Harbin Cargo needs a business card design.

Design a double-sided business card for new freight business. On the front, would like to see our logo along with the following info:

Nathaniel Voskuhl
CEO/FOUNDER
617-552-0194
nathanielvoskuhl@harbin-cargo.example

On the reverse side, we would like to use the graphic image of our logo only without the Harbin Cargo name.

```html
<!DOCTYPE html>
<html lang="en">
<head>
<meta charset="utf-8">
<title>Harbin Cargo — Business Card</title>
<link rel="stylesheet" href="https://fonts.googleapis.com/css2?family=Sora:wght@700&family=Roboto:wght@400&display=swap">
<style>
  :root {
    --backdrop: #9a9a9a;
    --paper: #f6f6f4;
    --navy: #2b2d6e;
    --navy-deep: #1c1d5a;
    --navy-light: #33358a;
    --red: #c1272d;
    --edge: #8e1014;
    --ink: #3a3a3a;
  }
  * { margin: 0; padding: 0; box-sizing: border-box; }
  html, body {
    width: 1200px; height: 1006px; overflow: hidden;
    background: var(--backdrop);
  }
  .sheet {
    width: 1200px; height: 1006px;
    display: flex; flex-direction: column; align-items: center; justify-content: center;
    gap: 60px;
  }
  .card {
    width: 760px; height: 434px;
    position: relative;
    border-bottom: 4px solid var(--edge);
    box-shadow: 0 14px 30px rgba(0,0,0,.25);
  }
  .card--front { background: var(--paper); display: flex; align-items: center; }
  .brand {
    width: 340px; padding-left: 60px;
    font-family: "Sora", sans-serif; font-weight: 700;
    color: var(--navy); font-size: 34px; line-height: 1.05;
    letter-spacing: 2px; text-transform: uppercase;
    display: flex; align-items: center; gap: 14px;
  }
  .brand__dot { width: 18px; height: 18px; border-radius: 50%; background: var(--red); flex: none; }
  .divider { width: 2px; height: 150px; background: var(--red); margin: 0 30px 0 14px; }
  .details { font-family: "Roboto", sans-serif; color: var(--ink); }
  .details__name {
    font-family: "Sora", sans-serif; font-weight: 700;
    color: var(--navy); font-size: 25px;
  }
  .details__role {
    font-family: "Roboto", sans-serif; color: var(--red);
    font-size: 17px; letter-spacing: .5px; margin: 2px 0 22px;
  }
  .contact { list-style: none; font-size: 15.5px; line-height: 1.6; }
  .contact li { display: flex; align-items: center; gap: 8px; }
  .contact svg { width: 14px; height: 14px; flex: none; fill: var(--navy); }
  .card--back {
    background: radial-gradient(ellipse at 30% 30%, var(--navy-light), var(--navy-deep) 75%);
  }
  .back-pattern { position: absolute; inset: 0; }
  .back-mark {
    position: absolute; right: 230px; bottom: 90px;
    width: 60px; height: 60px; border-radius: 50%;
    background: var(--red);
  }
</style>
</head>
<body>
<main class="sheet">
  <section class="card card--front" aria-label="Card front">
    <div class="brand"><span class="brand__dot"></span><span>Harbin<br>Cargo</span></div>
    <div class="divider"></div>
    <div class="details">
      <h1 class="details__name">Nathaniel Voskuhl</h1>
      <p class="details__role">CEO/FOUNDER</p>
      <ul class="contact">
        <li><svg viewBox="0 0 16 16"><path d="M3.6 1.5l2.3 2.6-1.2 1.8a9 9 0 0 0 5.4 5.4l1.8-1.2 2.6 2.3-1.3 2A11.5 11.5 0 0 1 1.5 3z"/></svg>617-552-0194</li>
        <li><svg viewBox="0 0 16 16"><path d="M1 3h14v10H1zM2 4.2v.4l6 4.2 6-4.2v-.4zM2 6v6h12V6L8 10z"/></svg>nathanielvoskuhl@harbin-cargo.example</li>
        <li><svg viewBox="0 0 16 16"><circle cx="8" cy="8" r="7"/></svg>www.harbin-cargo.example</li>
      </ul>
    </div>
  </section>

  <section class="card card--back" aria-label="Card back">
    <div class="back-pattern" role="img" aria-label="Embossed repeating pattern of the company mark on navy"></div>
    <div class="back-mark" role="img" aria-label="Company mark"></div>
  </section>
</main>
</body>
</html>
```